Meadowlark Learning Growth Partners (MLGP)

This is a professional business card. Logo and picture are a must on the front of the card. I am an educational consultant. I have been consulting for the past three years for a company. I am now opening my own company. My goal for my consulting company is to eventually consult all over America.

Target Market(s)

Educators, schools, professionals

Industry/Entity Type

Consulting

Contact Information for Business Card

Picture/logo on front, simple modern design

Font styles to use
Serif

Colors
85abd2
0355a3
3176b5
cedeed

Requirements
Must have
• picture, logo,
• Odessa Pruitt, Ed.S
• address 5073 Cormorant ridge Dr. Nashville, TN 37940
• Cell:616-555-0148
• Office: 629-555-0172
• www.Mlgpedu.example
• pruittodessa@mailbox.example

```html
<!DOCTYPE html>
<html lang="en">
<head>
<meta charset="utf-8">
<title>Meadowlark Learning Growth Partners – Business Card</title>
<link rel="stylesheet" href="https://fonts.googleapis.com/css2?family=Libre+Baskerville:wght@400;700&display=swap">
<style>
  :root {
    --navy-deep: #0a1a5c;
    --navy: #13287a;
    --royal: #0355a3;
    --mid-blue: #3176b5;
    --sky: #85abd2;
    --mist: #cedeed;
    --white: #ffffff;
    --page: #eef1f5;
  }
  * { box-sizing: border-box; margin: 0; padding: 0; }
  html, body {
    width: 1200px; height: 892px; overflow: hidden;
    background: var(--page);
    font-family: "Libre Baskerville", Georgia, serif;
  }
  .stage {
    width: 1200px; height: 892px;
    display: flex; align-items: center; justify-content: center; gap: 60px;
  }
  .card {
    position: relative;
    width: 520px; height: 298px;
    overflow: hidden;
    background: linear-gradient(135deg, var(--navy-deep) 0%, var(--navy) 45%, var(--royal) 100%);
    box-shadow: 0 8px 24px rgba(10, 26, 92, 0.25);
    color: var(--white);
  }
  .card__pattern {
    position: absolute; inset: 0;
    background:
      radial-gradient(ellipse at 70% 45%, rgba(133,171,210,0.55) 0%, rgba(49,118,181,0.35) 35%, rgba(3,85,163,0) 70%),
      linear-gradient(160deg, rgba(49,118,181,0.4) 0%, rgba(10,26,92,0) 60%);
  }
  /* front */
  .card--front .photo-frame {
    position: absolute; left: 26px; top: 24px;
    width: 250px; height: 186px;
    padding: 10px;
    background: rgba(133,171,210,0.35);
  }
  .card--front .photo {
    width: 100%; height: 100%;
    background: linear-gradient(180deg, var(--mid-blue) 0%, var(--royal) 60%, var(--navy) 100%);
  }
  .brand {
    position: absolute;
    display: flex; align-items: center; gap: 8px;
    font-weight: 700; color: var(--white); letter-spacing: 0.08em;
  }
  .brand__dot { border-radius: 50%; background: var(--white); }
  .card--front .brand { right: 34px; bottom: 30px; font-size: 30px; }
  .card--front .brand__dot { width: 22px; height: 22px; }
  /* back */
  .card--back .details {
    position: absolute; left: 28px; top: 26px; width: 300px;
  }
  .name {
    font-weight: 700; font-size: 21px; line-height: 1.05;
    text-transform: uppercase; letter-spacing: 0.02em;
  }
  .address { margin-top: 14px; font-size: 12.5px; line-height: 1.4; }
  .phones { margin-top: 12px; font-size: 12.5px; line-height: 1.4; }
  .phones .cell { font-weight: 700; }
  .web { margin-top: 14px; font-size: 12.5px; line-height: 1.45; }
  .web .site { font-weight: 700; }
  .card--back .brand { right: 16px; bottom: 14px; font-size: 11px; gap: 5px; }
  .card--back .brand__dot { width: 9px; height: 9px; }
  .card--back .panel-lines {
    position: absolute; right: 0; top: 0; width: 200px; height: 100%;
  }
</style>
</head>
<body>
<main class="stage">
  <section class="card card--front" aria-label="Business card front">
    <div class="card__pattern" role="img" aria-label="Abstract blue geometric background"></div>
    <div class="photo-frame">
      <div class="photo" role="img" aria-label="Portrait photo of Odessa Pruitt"></div>
    </div>
    <div class="brand"><span class="brand__dot"></span>MLGP</div>
  </section>

  <section class="card card--back" aria-label="Business card back">
    <div class="card__pattern" role="img" aria-label="Abstract blue geometric background"></div>
    <svg class="panel-lines" viewBox="0 0 200 298" aria-hidden="true">
      <line x1="0" y1="0" x2="0" y2="298" stroke="#85abd2" stroke-opacity="0.35" stroke-width="2"/>
      <line x1="190" y1="0" x2="190" y2="298" stroke="#0a1a5c" stroke-width="14"/>
    </svg>
    <div class="details">
      <h1 class="name">Odessa<br>Pruitt, Ed.S</h1>
      <p class="address">Cormorant ridge 5073<br>Dr. Nashville, TN 37940</p>
      <p class="phones"><span class="cell">Cell:616-555-0148</span><br>Office: 629-555-0172</p>
      <p class="web"><span class="site">www.Mlgpedu.example</span><br>pruittodessa@mailbox.example</p>
    </div>
    <div class="brand"><span class="brand__dot"></span>MLGP</div>
  </section>
</main>
</body>
</html>
```